Luma Vale Hotel Flyer

Design a tri-fold flyer for Luma Vale hotel in western Uganda that will be distributed to tour operators, as well as prospective and current guests. The flyer should highlight the natural serene environment, landscaped gardens, spacious luxurious rooms, local culture and proximity to tourist attractions . The flyer should follow the brand colors and logo in attached guidelines and include some of the text and suphotos provided.

```html
<!DOCTYPE html>
<html lang="en">
<head>
<meta charset="utf-8">
<title>Luma Vale Village – Tri-fold Flyer</title>
<link href="https://fonts.googleapis.com/css2?family=Montserrat:wght@400;500;800;900&family=Open+Sans:wght@400;600&display=swap" rel="stylesheet">
<style>
  :root{
    --backdrop:#8a8a8a;
    --charcoal:#3b3b3d;
    --ink:#1f1f1f;
    --red:#b01f24;
    --orange:#ef5a24;
    --tan:#b8a77e;
    --grey-soft:#d6d6d6;
    --white:#ffffff;
  }
  *{box-sizing:border-box;margin:0;padding:0}
  html,body{width:795px;height:1200px;overflow:hidden;background:var(--backdrop)}
  .canvas{position:relative;width:795px;height:1200px;overflow:hidden;background:var(--backdrop)}
  .stage{position:absolute;left:0;top:0;width:1400px;height:2112px;transform:scale(.56786);transform-origin:0 0}
  .sheet{position:absolute;left:166px;width:1068px;height:824px;display:flex}
  .sheet--outside{top:186px}
  .sheet--inside{top:1106px}
  .panel{position:relative;width:356px;height:824px;overflow:hidden}
  .layer{position:absolute;left:0;top:0;width:356px;height:824px}
  .body-text{font-family:"Open Sans",sans-serif;font-size:14.6px;line-height:19px;color:var(--white)}
  .heading{font-family:"Montserrat",sans-serif;font-weight:800;text-transform:uppercase}
  .brand-name{font-family:"Montserrat",sans-serif;font-weight:800;color:var(--ink);display:flex;align-items:center;justify-content:center;gap:12px;position:absolute;left:0;width:356px}
  .brand-dot{width:18px;height:18px;border-radius:50%;background:var(--orange)}

  /* outside – intro */
  .panel--intro{background:var(--charcoal)}
  .intro-copy{position:absolute;left:33px;top:42px;width:295px}
  .intro-copy p+p{margin-top:10px}

  /* outside – testimonials & contact */
  .panel--contact{background:var(--white)}
  .section-title{position:absolute;left:38px;width:272px;border-top:1px solid #555;border-bottom:1px solid #555;color:var(--orange);font-size:25px;padding:6px 0 4px}
  .testimonial{position:absolute;left:38px;top:112px;width:274px;font-family:"Open Sans",sans-serif;font-size:14.3px;line-height:19px;color:var(--ink)}
  .quote-mark{position:absolute;font-family:Georgia,serif;font-size:64px;line-height:1;color:#9a9a9a;font-weight:700}
  .cta{position:absolute;left:38px;top:470px;color:var(--white);font-size:33px;line-height:44px;letter-spacing:.3px}
  .cta-sub{position:absolute;left:38px;top:658px;width:270px;border-top:1px solid rgba(255,255,255,.7);border-bottom:1px solid rgba(255,255,255,.7);padding:6px 0 7px;font-family:"Montserrat",sans-serif;font-weight:500;font-size:15px;color:var(--white)}
  .contact-list{position:absolute;left:38px;top:701px;list-style:none}
  .contact-list li{display:flex;align-items:center;gap:9px;height:24.7px;font-family:"Open Sans",sans-serif;font-size:14.5px;color:var(--white)}
  .contact-list svg{width:13px;height:13px;flex:none}

  /* outside – cover */
  .panel--cover{background:var(--white)}
  .welcome-tag{position:absolute;left:46px;top:579px;width:214px;height:33px;background:var(--orange);color:var(--white);font-family:"Montserrat",sans-serif;font-weight:400;font-size:25px;line-height:33px;text-align:center;letter-spacing:.5px}
  .cover-title{position:absolute;left:44px;top:612px;color:var(--ink);font-size:55px;line-height:53px;letter-spacing:.5px}
  .cover-web{position:absolute;left:46px;top:776px;font-family:"Open Sans",sans-serif;font-size:14.5px;color:var(--white)}
  .cover-web b{font-weight:600}

  /* inside – attractions */
  .panel--attractions{background:var(--charcoal)}
  .attractions-title{position:absolute;left:34px;top:44px;width:272px;border-top:1px solid #8a8a8a;border-bottom:1px solid #8a8a8a;padding:10px 0 8px;color:var(--orange);font-size:33px;line-height:35px}
  .attractions-list{position:absolute;left:34px;top:155px;width:290px;list-style:none}
  .attractions-list li{position:relative;padding-left:22px;font-family:"Open Sans",sans-serif;font-size:14.5px;line-height:20px;color:var(--white);margin-bottom:4.3px}
  .attractions-list li::before{content:"";position:absolute;left:1px;top:5px;width:6px;height:6px;border:2px solid var(--orange);border-radius:50%}

  /* inside – restaurant */
  .restaurant-title{position:absolute;left:36px;top:365px;color:var(--white);font-size:35px;line-height:38px}
  .restaurant-sub{position:absolute;left:36px;top:448px;font-family:"Montserrat",sans-serif;font-weight:400;font-size:18.5px;color:#f6d9d9}

  /* inside – culture */
  .culture-title{position:absolute;left:43px;top:678px;color:var(--white);font-size:35px}
  .culture-copy{position:absolute;left:43px;top:724px;width:290px;font-family:"Montserrat",sans-serif;font-weight:400;font-size:18px;line-height:23px;color:#fde3d6}
  .chevron{position:absolute}
</style>
</head>
<body>
<div class="canvas">
<div class="stage">

  <!-- Outside spread -->
  <section class="sheet sheet--outside">

    <article class="panel panel--intro">
      <svg class="layer" viewBox="0 0 356 824">
        <defs>
          <linearGradient id="veranda" x1="0" y1="0" x2="1" y2="1">
            <stop offset="0" stop-color="#5f8f3a"/>
            <stop offset=".55" stop-color="#cfc79a"/>
            <stop offset="1" stop-color="#3b3f4a"/>
          </linearGradient>
        </defs>
        <rect x="0" y="280" width="356" height="544" fill="url(#veranda)" role="img" aria-label="Photo: veranda with wicker chairs overlooking green gardens"/>
        <path d="M0 330 C60 300 110 290 160 300 C220 312 250 330 300 310 C325 300 345 294 356 296 V0 H0 Z" fill="var(--charcoal)"/>
      </svg>
      <div class="intro-copy body-text">
        <p>Nestled on 18 acres of beautifully landscaped grounds, our hotel offers 16 spacious luxury rooms, restaurant, jungle playground, nature walks, serene gardens, souvenir shop, meditation chapel, and cultural performances.</p>
        <p>Situated close to Fort Portal tourist hub, Luma Vale is ideally located for birding, hiking, chimpanzee tracking, and visits to hot springs, caves and crater lakes - a perfect haven for nature lovers, business travellers and adventurers alike.</p>
      </div>
    </article>

    <article class="panel panel--contact">
      <h2 class="section-title heading" style="top:44px">Testimonials</h2>
      <span class="quote-mark" style="left:36px;top:100px">&ldquo;</span>
      <p class="testimonial">&nbsp;&nbsp;&nbsp;&nbsp;&nbsp;&nbsp;&nbsp;&nbsp;Everything! The natural ambiance, gardens, extra large room in the beautifully designed bungalow, the peace, tranquility ... I had an absolutely wonderful and pleasant stay in this amazing beautiful and peaceful place. Could not ask for more for a place to stay and host to look after you.</p>
      <span class="quote-mark" style="left:272px;top:262px">&rdquo;</span>
      <div class="brand-name" style="top:338px;font-size:44px">Luma Vale<span class="brand-dot"></span></div>
      <svg class="layer" viewBox="0 0 356 824">
        <path d="M0 450 C60 425 120 408 180 416 C240 424 300 458 356 444 V824 H0 Z" fill="var(--red)"/>
      </svg>
      <h2 class="cta heading">Feel like<br>having the<br>Luma Vale<br>experience?</h2>
      <p class="cta-sub">CONTACT US NOW</p>
      <ul class="contact-list">
        <li><svg viewBox="0 0 12 12"><path d="M6 11 C3 7.5 2 6 2 4.5 A4 4 0 0 1 10 4.5 C10 6 9 7.5 6 11 Z" fill="none" stroke="#fff" stroke-width="1"/><circle cx="6" cy="4.5" r="1.4" fill="none" stroke="#fff"/></svg>Orchard Lane, Fort Portal, Uganda.</li>
        <li><svg viewBox="0 0 12 12"><rect x="1" y="2.5" width="10" height="7" fill="none" stroke="#fff"/><path d="M1 2.5 L6 6.5 L11 2.5" fill="none" stroke="#fff"/></svg>lumavalevillage@mail.example</li>
        <li><svg viewBox="0 0 12 12"><path d="M3 1.5 L5 4 L4 5.2 C4.6 6.6 5.4 7.4 6.8 8 L8 7 L10.5 9 L9.3 10.5 C5.5 10 2 6.5 1.5 2.7 Z" fill="none" stroke="#fff"/></svg>+256 700 410 228</li>
        <li><svg viewBox="0 0 12 12"><circle cx="6" cy="6" r="4.8" fill="none" stroke="#fff"/><ellipse cx="6" cy="6" rx="2" ry="4.8" fill="none" stroke="#fff"/><path d="M1.2 6 H10.8" stroke="#fff"/></svg>www.lumavale.example</li>
      </ul>
    </article>

    <article class="panel panel--cover">
      <div class="brand-name" style="top:52px;font-size:52px">Luma Vale<span class="brand-dot"></span></div>
      <svg class="layer" viewBox="0 0 356 824">
        <defs>
          <linearGradient id="bungalow" x1="0" y1="0" x2="0" y2="1">
            <stop offset="0" stop-color="#3f8fd6"/>
            <stop offset=".45" stop-color="#8d8d84"/>
            <stop offset="1" stop-color="#6f9a3a"/>
          </linearGradient>
        </defs>
        <path d="M0 190 C40 175 70 180 110 188 V210 H0 Z" fill="var(--red)"/>
        <path d="M230 190 C270 176 320 180 356 188 V215 H230 Z" fill="var(--red)"/>
        <path d="M0 200 C60 190 100 160 160 172 C220 184 250 200 300 186 C330 178 345 176 356 178 V560 C320 548 280 532 230 544 C180 556 120 560 60 538 C35 530 15 532 0 540 Z" fill="url(#bungalow)" role="img" aria-label="Photo: round two-storey stone bungalow with red window frames in a garden"/>
        <path d="M0 528 C30 520 50 545 80 550 V560 H0 Z" fill="var(--red)"/>
        <path d="M300 536 C320 530 340 540 356 548 V560 H300 Z" fill="var(--red)"/>
        <path d="M0 760 C40 748 80 745 120 752 C160 760 200 740 240 736 C280 733 320 752 356 744 V824 H0 Z" fill="var(--tan)"/>
        <path d="M250 742 C290 730 330 736 356 750 V760 C330 748 300 744 270 750 Z" fill="#8c8c8c"/>
        <path d="M60 752 C100 738 140 742 160 752 C130 748 100 750 80 758 Z" fill="#8c8c8c"/>
      </svg>
      <svg class="chevron" style="left:262px;top:536px" width="50" height="56" viewBox="0 0 50 56"><path d="M28 2 L4 28 L28 54 H46 L22 28 L46 2 Z" fill="var(--ink)"/><path d="M18 16 L10 28 L18 40" fill="none" stroke="var(--white)" stroke-width="4"/></svg>
      <div class="welcome-tag">WELCOME TO</div>
      <h1 class="cover-title heading">Luma Vale<br>Village</h1>
      <p class="cover-web">www.<b>lumavale</b>.example</p>
    </article>
  </section>

  <!-- Inside spread -->
  <section class="sheet sheet--inside">

    <article class="panel panel--attractions">
      <h2 class="attractions-title heading">Nearby<br>attractions</h2>
      <ul class="attractions-list">
        <li>Chimpanzee tracking in Kibale tropical forest</li>
        <li>Hiking in the Rwenzori Mountains</li>
        <li>Stunning views of over 50 crater lakes</li>
        <li>Sempaya hot springs</li>
        <li>Waterfalls and caves</li>
        <li>Birding in Bigodi Wetland Sanctuary</li>
        <li>Game drives and boating in Semuliki wildlife reserve</li>
        <li>Kazinga (Queen Elizabeth) park known for its rich biodiversity</li>
        <li>Lush tea plantations on rolling hills</li>
        <li>Vanilla farm tours</li>
      </ul>
      <svg class="layer" viewBox="0 0 356 824">
        <defs>
          <linearGradient id="chapel" x1="0" y1="0" x2="1" y2="1">
            <stop offset="0" stop-color="#9a2a2a"/>
            <stop offset=".45" stop-color="#4f7a3a"/>
            <stop offset="1" stop-color="#7a6a52"/>
          </linearGradient>
        </defs>
        <path d="M0 520 C50 505 90 480 140 482 C200 485 240 510 290 505 C320 502 340 495 356 490 V824 H0 Z" fill="url(#chapel)" role="img" aria-label="Photo: A-frame meditation chapel with stained glass among trees and red foliage"/>
      </svg>
    </article>

    <article class="panel panel--restaurant">
      <svg class="layer" viewBox="0 0 356 824">
        <defs>
          <linearGradient id="swing" x1="0" y1="0" x2="0" y2="1">
            <stop offset="0" stop-color="#4f6a34"/>
            <stop offset="1" stop-color="#8f7a5c"/>
          </linearGradient>
          <linearGradient id="courtyard" x1="0" y1="0" x2="0" y2="1">
            <stop offset="0" stop-color="#6f6a5e"/>
            <stop offset=".5" stop-color="#d9d2bf"/>
            <stop offset="1" stop-color="#8a7f70"/>
          </linearGradient>
        </defs>
        <rect x="0" y="0" width="356" height="340" fill="url(#swing)" role="img" aria-label="Photo: child on a swing in the garden"/>
        <rect x="0" y="500" width="356" height="324" fill="url(#courtyard)" role="img" aria-label="Photo: courtyard restaurant terrace with parasols, tables and chairs"/>
        <path d="M0 310 C40 300 70 320 110 330 C160 342 200 310 250 312 C300 314 330 336 356 334 V510 C320 518 290 498 250 506 C200 516 160 542 100 530 C60 522 30 505 0 512 Z" fill="var(--red)"/>
      </svg>
      <h2 class="restaurant-title heading">Courtyard<br>restaurant</h2>
      <p class="restaurant-sub">Enjoy local and western cuisine</p>
    </article>

    <article class="panel panel--culture">
      <svg class="layer" viewBox="0 0 356 824">
        <defs>
          <linearGradient id="dance" x1="0" y1="0" x2="1" y2="1">
            <stop offset="0" stop-color="#b9a98c"/>
            <stop offset=".5" stop-color="#c23a30"/>
            <stop offset="1" stop-color="#5c4a3a"/>
          </linearGradient>
        </defs>
        <rect x="0" y="0" width="356" height="660" fill="url(#dance)" role="img" aria-label="Photo: performer in red costume during a live cultural dance"/>
        <path d="M0 640 C40 632 70 612 110 614 C160 618 190 640 240 640 C290 640 320 618 356 620 V824 H0 Z" fill="var(--orange)"/>
      </svg>
      <svg class="chevron" style="left:274px;top:670px" width="48" height="54" viewBox="0 0 50 56"><path d="M28 2 L4 28 L28 54 H46 L22 28 L46 2 Z" fill="var(--ink)"/><path d="M18 16 L10 28 L18 40" fill="none" stroke="var(--white)" stroke-width="4"/></svg>
      <h2 class="culture-title heading">Culture</h2>
      <p class="culture-copy">Experience the excitement of our live cultural performances!</p>
    </article>
  </section>

</div>
</div>
</body>
</html>
```